Logo Tweak & Full Set of Stationery

We need a redesign / tweaking of Logo for rebranding of our company. We are Australia's largest installer of commercial fencing and high security infrastructure. We also have divisions in security and civil works (infrastrucuture).

We would like to see designs that incorporate black, white & blue. Revamp of current Diamond Logo (including HC) would be ideal but open to all ideas.

Design needs to portray a highly professional & corporate image.

Required:
- Tweak / Redesign of Logo
- Letterhead
- email Signature
- Business Cards
- Presentation Folder

Address fields should be interchangeable to accomodate multiple locations.

Website: www.harvillecorp.com.au
Updates

Due to short turn around time for project - Fee increased to $500 AUD Guaranteed

Thanks

Designs are looking good
I have emailed those submitted thus far to the board to start short listing.

Please do not take offence if your design is eliminated as part of this process  - there are so many great concepts and if is difficult to pick between them.

Thanks
Dustin

Target Market(s)

Tier 1 / 2 Builders (ie.. Brick Arch Peter Farley) and Government related bodies

Industry/Entity Type

Security

Requirements
Must have
• Company Name: Harville Corp

Tag Line: Fencing * Security * Civil

Logo

```html
<!DOCTYPE html>
<html lang="en">
<head>
<meta charset="utf-8">
<title>Harville Corp – Identity &amp; Business Card</title>
<link href="https://fonts.googleapis.com/css2?family=Roboto+Slab:wght@300;800&family=Roboto:wght@400;500;700&display=swap" rel="stylesheet">
<style>
  :root {
    --brand-grey: #b6b7b9;
    --brand-grey-light: #bfc0c2;
    --stage-grey: #e1e2e3;
    --card-blue: #00aeef;
    --card-teal: #10a89c;
    --white: #ffffff;
    --ink-dark: #6d6e71;
    --ink-body: #8a8b8e;
  }
  * { margin: 0; padding: 0; box-sizing: border-box; }
  html, body { width: 1200px; height: 846px; overflow: hidden; background: var(--white); }
  .canvas { position: relative; width: 1200px; height: 846px; font-family: "Roboto", Arial, sans-serif; }

  .logo-stage { position: absolute; left: 0; top: 0; width: 1200px; height: 406px; background: var(--white); }
  .logo-lockup { position: absolute; left: 0; right: 0; top: 80px; text-align: center; }
  .logo-square { display: block; margin: 0 auto; width: 133px; height: 133px; border: 7px solid var(--brand-grey); border-radius: 22px; }
  .logo-name { margin-top: 12px; font-family: "Roboto Slab", Georgia, serif; font-weight: 800; font-size: 96px; line-height: 1; color: var(--brand-grey); letter-spacing: 1px; }
  .logo-entity { margin-top: 8px; font-family: "Roboto Slab", Georgia, serif; font-weight: 300; font-size: 46px; line-height: 1; color: var(--brand-grey-light); letter-spacing: 1px; }

  .card-stage { position: absolute; left: 0; top: 406px; width: 1200px; height: 440px; background: var(--stage-grey); }
  .card { position: absolute; top: 53px; width: 516px; height: 314px; box-shadow: 0 2px 6px rgba(0,0,0,0.18); text-align: center; }
  .card-front { left: 70px; background: linear-gradient(180deg, var(--card-blue) 0%, var(--card-teal) 100%); color: var(--white); }
  .card-back { left: 610px; background: var(--white); color: var(--ink-body); }

  .front-square { display: block; margin: 37px auto 0; width: 60px; height: 60px; border: 4px solid var(--white); border-radius: 11px; }
  .front-name { margin-top: 10px; font-family: "Roboto Slab", Georgia, serif; font-weight: 800; font-size: 38px; line-height: 1; }
  .front-entity { margin-top: 3px; font-family: "Roboto Slab", Georgia, serif; font-weight: 300; font-size: 20px; line-height: 1; }
  .person-name { margin-top: 18px; font-weight: 500; font-size: 25px; line-height: 1; }
  .person-role { margin-top: 5px; font-size: 10px; letter-spacing: 0.5px; }
  .front-contact { margin-top: 20px; font-size: 15px; line-height: 20px; }
  .front-contact b { font-weight: 700; }

  .back-heading { margin-top: 31px; font-weight: 700; font-size: 17.5px; line-height: 23px; color: var(--ink-dark); }
  .back-services { margin-top: 20px; font-size: 10.5px; line-height: 15.4px; }
  .back-contact { margin-top: 19px; font-size: 12.5px; line-height: 18px; color: var(--ink-dark); }
  .back-contact b { font-weight: 700; }
</style>
</head>
<body>
<div class="canvas">
  <section class="logo-stage">
    <div class="logo-lockup">
      <span class="logo-square" aria-hidden="true"></span>
      <div class="logo-name">Harville Corp</div>
      <div class="logo-entity">Australia Pty Ltd</div>
    </div>
  </section>

  <section class="card-stage">
    <article class="card card-front">
      <span class="front-square" aria-hidden="true"></span>
      <div class="front-name">Harville Corp</div>
      <div class="front-entity">Australia Pty Ltd</div>
      <div class="person-name">Dustin Marsh</div>
      <div class="person-role">CHIEF FINANCIAL OFFICER</div>
      <div class="front-contact">
        dmarsh@harvillecorp.com.au<br>
        <b>M:</b> +61 4 5550 1234
      </div>
    </article>

    <article class="card card-back">
      <h2 class="back-heading">Harville Corp Specialise in ALL types<br>of Fencing &amp; Security Systems</h2>
      <p class="back-services">
        Palisade Fencing, Tubular Security Fencing, CF358 Security Mesh,<br>
        Chainwire Fencing (permanent &amp; temporary), Guard Rails and Handrails,<br>
        Internal Chainwire Enclosures, Weldmesh Fencing and Enclosures,<br>
        Non-Destructive Digging, Livestock and Fauna Fencing, Access Control,<br>
        Security Systems, Bollards, Security Lighting, Alarm Systems, Civil Works,<br>
        Type 1-6 SRA Approved Pedestrian Fencing, Wire Rope Vehicle Fencing,<br>
        Rock Fall Fencing, Electronic Fencing and ALL Styles of Gates to suit.
      </p>
      <p class="back-contact">
        <b>FREE CALL:</b> 1800 555 010<br>
        <b>T:</b> +61 2 5550 8146 &nbsp; <b>F:</b> +61 2 5550 7505<br>
        www.harvillecorp.com.au
      </p>
    </article>
  </section>
</div>
</body>
</html>
```